BrambleWorks business card

Looking for business card design that supports our company/software values. We have 2 logo designs at the moment but open to change if you think you can enhance the brand. Check out website www.brambleworks.com.au.

Target Market(s)

Education

Contact Information for Business Card

Name, title, mobile, email and website

Font styles to use
Sans Serif

Colors

Designer to choose colors to be used in the design.

Requirements
Must have
• BrambleWorks logo with tree and tagline on rear side with dark grey background colour

```html
<!DOCTYPE html>
<html lang="en">
<head>
<meta charset="utf-8">
<title>BrambleWorks business card</title>
<link href="https://fonts.googleapis.com/css2?family=Ubuntu:wght@400;500;700&display=swap" rel="stylesheet">
<style>
  :root {
    --backdrop: #e9e9e9;
    --paper: #ffffff;
    --leaf-green: #2f5f2b;
    --charcoal: #1d1b1c;
    --ink: #1a1a1a;
    --amber: #e9a219;
    --light-text: #f2f2f2;
  }
  * { margin: 0; padding: 0; box-sizing: border-box; }
  html, body { width: 1200px; height: 863px; overflow: hidden; }
  body {
    background: var(--backdrop);
    font-family: "Ubuntu", sans-serif;
    position: relative;
  }
  .card {
    position: absolute;
    top: 151px;
    width: 340px;
    height: 560px;
    background: var(--paper);
    overflow: hidden;
    box-shadow: 0 10px 30px rgba(0,0,0,0.18);
  }
  .card--front { left: 220px; }
  .card--back { left: 640px; }
  .card__base {
    position: absolute;
    left: 0; top: 0;
    width: 340px; height: 560px;
  }
  .wordmark {
    position: absolute;
    left: 0; right: 0;
    text-align: center;
    font-weight: 500;
    color: var(--ink);
    display: flex;
    align-items: center;
    justify-content: center;
    gap: 12px;
  }
  .wordmark__dot {
    width: 22px; height: 22px;
    border-radius: 50%;
    background: var(--leaf-green);
  }
  .card--front .wordmark { top: 120px; font-size: 30px; }
  .card--back .wordmark { top: 175px; font-size: 38px; }
  .holder {
    position: absolute;
    right: 26px;
    top: 288px;
    text-align: right;
    color: var(--ink);
  }
  .holder__name { font-weight: 700; font-size: 21px; letter-spacing: 0.5px; }
  .holder__title { font-size: 20px; line-height: 1; }
  .contacts {
    position: absolute;
    left: 28px;
    top: 428px;
    list-style: none;
    color: var(--light-text);
    font-size: 13px;
  }
  .contacts li {
    display: flex;
    align-items: center;
    gap: 12px;
    height: 30px;
  }
  .contacts svg { width: 16px; height: 16px; flex: none; }
  .tagline {
    position: absolute;
    left: 0; right: 0;
    top: 450px;
    text-align: center;
    font-weight: 500;
    font-size: 17px;
    line-height: 1.15;
  }
  .tagline__mark {
    width: 24px; height: 24px;
    border-radius: 50%;
    background: var(--amber);
    margin: 0 auto 10px;
  }
  .tagline__lead { color: var(--amber); display: block; }
  .tagline__rest { color: var(--light-text); display: block; }
</style>
</head>
<body>

  <section class="card card--front" aria-label="Business card front">
    <svg class="card__base" viewBox="0 0 340 560" aria-hidden="true">
      <path d="M0,350 C90,330 220,330 340,380 L340,560 L0,560 Z" fill="var(--leaf-green)"/>
      <path d="M0,372 C110,345 240,355 340,420 L340,560 L0,560 Z" fill="var(--charcoal)"/>
    </svg>
    <div class="wordmark"><span class="wordmark__dot"></span>BrambleWorks</div>
    <div class="holder">
      <div class="holder__name">MARCUS HALE</div>
      <div class="holder__title">owner</div>
    </div>
    <ul class="contacts">
      <li>
        <svg viewBox="0 0 16 16" aria-hidden="true"><path d="M2 6 Q8 1 14 6 L12.5 8 L10.5 6.5 L10.5 5 Q8 4 5.5 5 L5.5 6.5 L3.5 8 Z M4 9 H12 L13 14 H3 Z" fill="var(--amber)"/></svg>
        012 555 0198
      </li>
      <li>
        <svg viewBox="0 0 16 16" aria-hidden="true"><rect x="1" y="3" width="14" height="10" fill="var(--amber)"/><path d="M1 3 L8 9 L15 3" fill="none" stroke="var(--charcoal)" stroke-width="1.2"/></svg>
        email@brambleworks.com.au
      </li>
      <li>
        <svg viewBox="0 0 16 16" aria-hidden="true"><circle cx="8" cy="8" r="6.5" fill="none" stroke="var(--amber)" stroke-width="1.6"/><ellipse cx="8" cy="8" rx="2.8" ry="6.5" fill="none" stroke="var(--amber)" stroke-width="1.2"/><path d="M1.5 8 H14.5" stroke="var(--amber)" stroke-width="1.2"/></svg>
        www.brambleworks.com.au
      </li>
    </ul>
  </section>

  <section class="card card--back" aria-label="Business card back">
    <svg class="card__base" viewBox="0 0 340 560" aria-hidden="true">
      <path d="M0,330 C80,300 220,310 340,340 L340,560 L0,560 Z" fill="var(--leaf-green)"/>
      <path d="M0,370 C90,320 250,315 340,345 L340,560 L0,560 Z" fill="var(--charcoal)"/>
    </svg>
    <div class="wordmark">BrambleWorks</div>
    <div class="tagline">
      <div class="tagline__mark"></div>
      <span class="tagline__lead">Learner Progress</span>
      <span class="tagline__rest">Suite</span>
    </div>
  </section>

</body>
</html>
```